TalkBridge - Language Coaching Services

Sleek, innovative, trendy design for Language Coaching business.

TalkBridge is a new UK based company that provides Language Coaching services. We offer highly personalized on-line and face to face language courses. We also impart learning techniques workshops based on the latest neuroscience research for second-language acquisition.

Target Market(s)

Industry/Entity Type

Consulting

Contact Information for Business Card

TalkBridge
ElenaVT@talkbridge-demo.co.uk
TalkBridge-demo.co.uk
London, UK

Font styles to use
Sans Serif

```html
<!DOCTYPE html>
<html lang="en">
<head>
<meta charset="utf-8">
<title>TalkBridge – Business Card</title>
<link href="https://fonts.googleapis.com/css2?family=Montserrat:wght@400;500;600;700&display=swap" rel="stylesheet">
<style>
  :root{
    --bg:#2c2c2e;
    --card:#f7f8f8;
    --brand:#1e7ea3;
    --brand-dark:#0f4f6e;
    --brand-light:#2a93b6;
    --ink:#1d2a33;
    --navy:#143e5a;
  }
  *{margin:0;padding:0;box-sizing:border-box}
  html,body{width:1200px;height:997px;overflow:hidden}
  body{background:var(--bg);font-family:"Montserrat",sans-serif;position:relative}

  .card{position:absolute;width:560px;height:320px;background:var(--card);overflow:hidden;
        box-shadow:0 14px 34px rgba(0,0,0,.45)}
  .card--front{left:320px;top:130px}
  .card--back{left:320px;top:540px}

  .band{position:absolute;left:0;right:0;bottom:0;height:16px}
  .band--front{background:linear-gradient(90deg,var(--brand-light),var(--brand-dark))}

  .mark-circle{position:absolute;border-radius:50%;border:6px solid var(--brand)}
  .card--front .mark-circle{width:120px;height:120px;left:190px;top:38px}
  .wordmark{position:absolute;color:var(--brand);font-weight:600;letter-spacing:1px;white-space:nowrap}
  .card--front .wordmark{font-size:52px;left:0;right:0;text-align:center;top:180px}

  .card--back .mark-circle{width:88px;height:88px;left:246px;top:22px;border-width:5px}
  .card--back .wordmark{font-size:36px;left:186px;top:120px}
  .rule{position:absolute;height:2px;background:var(--navy)}
  .rule--top{left:186px;right:34px;top:170px}
  .rule--name{left:150px;right:300px;top:206px}

  .holder{position:absolute;left:34px;top:188px}
  .holder__name{font-size:15px;font-weight:700;color:var(--navy);letter-spacing:.5px}
  .holder__role{font-size:12px;color:var(--ink);font-weight:500;margin-top:2px}

  .contacts{position:absolute;left:34px;top:238px;list-style:none}
  .contacts li{display:flex;align-items:center;gap:10px;font-size:13px;color:var(--ink);height:22px;font-weight:500}
  .contacts svg{width:16px;height:16px;flex:none}

  .website{position:absolute;right:28px;top:226px;font-size:13px;font-weight:700;color:var(--brand)}

  .band--back{height:18px;display:flex}
  .band--back .seg-light{width:46%;background:var(--brand-light);clip-path:polygon(0 0,100% 0,96% 100%,0 100%)}
  .band--back .seg-dark{flex:1;background:var(--brand-dark);margin-left:6px;clip-path:polygon(3% 0,100% 0,100% 100%,0 100%)}
</style>
</head>
<body>

  <section class="card card--front" aria-label="Business card front">
    <div class="mark-circle"></div>
    <div class="wordmark">TALKBRIDGE</div>
    <div class="band band--front"></div>
  </section>

  <section class="card card--back" aria-label="Business card back">
    <div class="mark-circle"></div>
    <div class="wordmark">TALKBRIDGE</div>
    <div class="rule rule--top"></div>

    <div class="holder">
      <div class="holder__name">ELENA VARGA</div>
      <div class="holder__role">Director</div>
    </div>
    <div class="rule rule--name"></div>

    <ul class="contacts">
      <li>
        <svg viewBox="0 0 16 16"><circle cx="8" cy="8" r="8" fill="#143e5a"/><path d="M5 4.5l1.6-.4.8 2-1 .7a5 5 0 002.8 2.8l.7-1 2 .8-.4 1.6c-3.4.2-6.7-3.1-6.5-6.5z" fill="#fff"/></svg>
        020.7946.0321
      </li>
      <li>
        <svg viewBox="0 0 16 16"><circle cx="8" cy="8" r="8" fill="#143e5a"/><rect x="4" y="5" width="8" height="6" fill="none" stroke="#fff" stroke-width="1"/><path d="M4 5l4 3.2L12 5" fill="none" stroke="#fff" stroke-width="1"/></svg>
        elenavt.talk
      </li>
      <li>
        <svg viewBox="0 0 16 16"><circle cx="8" cy="8" r="8" fill="#143e5a"/><path d="M8 3.5a3 3 0 00-3 3c0 2.2 3 5.8 3 5.8s3-3.6 3-5.8a3 3 0 00-3-3z" fill="#fff"/><circle cx="8" cy="6.5" r="1.1" fill="#143e5a"/></svg>
        ElenaVT@talkbridge-demo.co.uk
      </li>
    </ul>

    <div class="website">www.talkbridge-demo.co.uk</div>

    <div class="band band--back"><div class="seg-light"></div><div class="seg-dark"></div></div>
  </section>

</body>
</html>
```